Need a label for food product looking original design

We need two labels designed ( Front and Back ) for our new product Freeze Dried Strawberry Pieces On the front should also be our company name Velmaro . A pack will weigh 50 grams there should also be an image included of these strawbberies please find an attached file. Also it's suitable for vegans and vegetarians On the back there should be some information included what the product is used for and nutritional facts, also an e-mail for questions or product quality to be sent to sales@velmaro.co.uk Both labels should be 16cm long and 11cm wide we'll be using stand up pouches.

Target Market(s)

Bakery, snacks.

Font styles to use
Decorative
Script

Requirements
Must have
• Company name, image of the product.Label color to blend in pouch color.
Nice to have
• Suitable for vegans and vegetarians logos.
Should not have
• Custom printed pouches are not available.

```html
<!DOCTYPE html>
<html lang="en">
<head>
<meta charset="utf-8">
<title>Velmaro Freeze Dried Strawberry – Front Label</title>
<link rel="stylesheet" href="https://fonts.googleapis.com/css2?family=Bebas+Neue&family=Kaushan+Script&family=Oswald:wght@400;600&display=swap">
<style>
  :root {
    --canvas-bg: #ececec;
    --label-red: #c4161c;
    --label-red-dark: #9e1217;
    --label-red-light: #d3292e;
    --leaf-green: #7cb833;
    --photo-light: #f6f6f6;
    --photo-mid: #dcdcdc;
    --berry-tone: #e06a78;
    --type-light: #f3e9e9;
    --white: #ffffff;
  }
  html, body {
    margin: 0;
    padding: 0;
    width: 1038px;
    height: 1200px;
    overflow: hidden;
    background: var(--canvas-bg);
  }
  .label {
    position: absolute;
    left: 144px;
    top: 40px;
    width: 750px;
    height: 1120px;
    overflow: hidden;
    background: var(--photo-light);
  }
  .product-photo {
    position: absolute;
    left: 0;
    top: 0;
    width: 750px;
    height: 700px;
    background:
      radial-gradient(ellipse 300px 170px at 300px 260px, var(--berry-tone) 0%, rgba(224,106,120,0.55) 45%, rgba(224,106,120,0) 100%),
      linear-gradient(160deg, var(--photo-light) 0%, var(--photo-mid) 100%);
  }
  .label-shapes {
    position: absolute;
    left: 0;
    top: 0;
    width: 750px;
    height: 1120px;
  }
  .brand-name {
    position: absolute;
    left: 581px;
    top: 50px;
    font-family: "Oswald", sans-serif;
    font-weight: 600;
    font-size: 26px;
    color: var(--white);
    letter-spacing: 0.5px;
  }
  .title-freeze {
    position: absolute;
    left: 79px;
    top: 772px;
    font-family: "Oswald", sans-serif;
    font-weight: 400;
    font-size: 34px;
    letter-spacing: 16px;
    color: var(--type-light);
    line-height: 1;
  }
  .title-dried {
    position: absolute;
    left: 318px;
    top: 728px;
    font-family: "Kaushan Script", cursive;
    font-size: 84px;
    color: var(--type-light);
    line-height: 1;
  }
  .title-product {
    position: absolute;
    left: 72px;
    top: 826px;
    font-family: "Bebas Neue", sans-serif;
    font-size: 150px;
    letter-spacing: 1px;
    color: var(--type-light);
    line-height: 1;
  }
  .diet-divider {
    position: absolute;
    left: 52px;
    top: 985px;
    width: 3px;
    height: 110px;
    background: var(--leaf-green);
  }
  .diet-badge {
    position: absolute;
    left: 80px;
    top: 1000px;
    width: 120px;
    height: 72px;
    border-radius: 36px;
    background: var(--leaf-green);
  }
  .net-weight {
    position: absolute;
    left: 581px;
    top: 1028px;
    font-family: "Kaushan Script", cursive;
    font-size: 44px;
    color: var(--type-light);
    line-height: 1;
  }
</style>
</head>
<body>
  <main class="label">
    <div class="product-photo" role="img" aria-label="Photo of freeze dried strawberry slices piled in a metal scoop on a white surface"></div>

    <svg class="label-shapes" viewBox="0 0 750 1120" aria-hidden="true">
      <path class="corner-band" d="M454,0 L750,0 L750,230 Q610,120 454,0 Z" fill="var(--label-red)"/>
      <path class="green-sweep" d="M0,396 Q330,570 750,649 L750,1120 L0,1120 Z" fill="var(--leaf-green)"/>
      <path class="red-panel" d="M0,518 Q330,650 750,675 L750,1120 L0,1120 Z" fill="var(--label-red)"/>
      <path class="panel-stripe" d="M400,1120 L750,810 L750,862 L462,1120 Z" fill="var(--label-red-light)"/>
      <path class="panel-shade" d="M462,1120 L750,862 L750,1120 Z" fill="var(--label-red-dark)"/>
    </svg>

    <div class="brand-name">Velmaro</div>

    <div class="title-freeze">FREEZE</div>
    <div class="title-dried">Dried</div>
    <div class="title-product">STRAWBERRY</div>

    <div class="diet-divider"></div>
    <div class="diet-badge" role="img" aria-label="Suitable for vegans and vegetarians badge"></div>

    <div class="net-weight">50g</div>
  </main>
</body>
</html>
```